VantorGoods.example -Ecommerce Website for Luxury Products

This will be an ecommerce site. A website portal that will allow both consumers to enter one way and see specific purchase options and businesses to enter via a different link that allows B2B to see their specific options once logged into. B2C can purchase both as a guest/or after account is setup. B2B must be approved to set up account. This is front end website project. Back-end integration is separate. Will be hosted on Servalia with a domain registration held at NetBrindle. Additional website concept/idea/synergy can be found from sister site-KRWMLodging.example

```html
<!DOCTYPE html>
<html lang="en">
<head>
<meta charset="utf-8">
<title>VantorGoods – Home</title>
<link rel="stylesheet" href="https://fonts.googleapis.com/css2?family=Playfair+Display:wght@400;600;700&family=Poppins:wght@300;400;500;600&display=swap">
<style>
:root{
  --bg:#0f1716;
  --bg-deep:#0a100f;
  --panel:#151d1c;
  --gold:#b8935a;
  --gold-soft:#d2b27c;
  --brown:#8a6a45;
  --cream:#f2ede6;
  --text:#e9e6e0;
  --muted:#a9aca8;
  --line:#3a413f;
}
*{margin:0;padding:0;box-sizing:border-box}
html,body{width:1200px;height:3648px;overflow:hidden}
body{background:var(--bg);color:var(--text);font-family:"Poppins",sans-serif;position:relative}
.abs{position:absolute}
.serif{font-family:"Playfair Display",serif}
.media{position:absolute}
.btn{display:inline-block;font-size:13px;font-weight:500;letter-spacing:.5px;text-transform:uppercase;padding:9px 18px}
.stars{color:var(--gold);font-size:18px;letter-spacing:3px}
.rating{display:flex;align-items:center;gap:12px;font-size:14px;color:var(--text)}
.shop-link{display:flex;align-items:center;gap:12px;font-size:15px;font-weight:500;color:var(--text);border-bottom:1px solid var(--text);padding-bottom:4px;width:max-content}

/* header / hero */
.hero-media{left:0;top:0;width:1200px;height:700px;background:
  radial-gradient(ellipse 420px 260px at 880px 420px,#6b3f20 0%,#3a2213 45%,transparent 80%),
  radial-gradient(ellipse 300px 200px at 760px 150px,#3b3f3f 0%,transparent 75%),
  linear-gradient(180deg,#0c0f0f 0%,#121514 60%,var(--bg) 100%)}
.brand{left:68px;top:30px;font-family:"Playfair Display",serif;font-size:22px;color:var(--gold);font-weight:600}
.nav{left:490px;top:36px;display:flex;gap:52px;font-size:14px}
.nav a{color:var(--text);text-decoration:none}
.nav .active{border-bottom:2px solid var(--text);padding-bottom:6px}
.nav-icons{left:966px;top:32px;display:flex;gap:20px}
.hero-kicker{left:160px;top:214px;font-size:48px;font-weight:600;color:#fff}
.hero-title{left:160px;top:272px;font-size:90px;font-weight:600;color:#fff;line-height:1}
.hero-copy{left:160px;top:384px;width:440px;font-size:14px;line-height:1.45;color:var(--text)}
.hero-btn{left:160px;top:460px;border:1px solid #fff;color:#fff;background:transparent}

/* portal cards */
.portal{top:608px;width:420px;height:172px;border-radius:14px;text-align:center;padding-top:30px}
.portal h2{font-family:"Playfair Display",serif;font-size:28px;font-weight:600}
.portal p{font-size:14px;line-height:1.4;margin:6px auto 14px;width:300px}
.portal .btn{background:var(--brown);color:#fff;font-size:12px}
.portal-consumer{left:164px;background:var(--cream);color:#1a1a1a}
.portal-business{left:612px;background:var(--panel);border:1px solid var(--line);color:#fff}

/* story */
.story-head{left:0;top:828px;width:1200px;display:flex;align-items:center;justify-content:center;gap:22px}
.story-head span{display:block;width:110px;height:2px;background:var(--gold)}
.story-head h2{font-family:"Playfair Display",serif;font-size:50px;font-weight:600;color:var(--gold)}
.story-copy{left:290px;top:900px;width:620px;text-align:center;font-size:14px;line-height:1.45}

/* feature rows */
.feature-title{font-family:"Playfair Display",serif;font-size:40px;font-weight:600;display:flex;align-items:center;gap:18px}
.feature-title i{display:block;height:2px;background:currentColor}
.feature-copy{font-size:13px;line-height:1.5}

/* product cards */
.product{top:2760px;width:320px;height:420px;border-radius:18px;overflow:hidden}
.product .shade{position:absolute;left:0;right:0;bottom:0;height:210px;background:linear-gradient(180deg,transparent,rgba(8,10,10,.92) 45%)}
.product .info{position:absolute;left:0;right:0;bottom:24px;text-align:center}
.product h3{font-family:"Playfair Display",serif;font-size:32px;font-weight:600;color:#fff}
.product .stars{display:block;margin-top:6px}
.product small{display:block;font-size:14px;margin:4px 0 14px}
.product .btn{background:#fff;color:#111;width:200px}
.view-all{left:522px;top:3232px;background:#3b3a36;color:#fff;border-radius:2px}

/* footer */
.footer-rule{left:160px;top:3328px;width:880px;height:1px;background:var(--line)}
.footer-brand{left:200px;top:3390px;font-family:"Playfair Display",serif;font-size:26px;color:var(--gold);font-weight:600}
.socials{left:208px;top:3524px;display:flex;gap:24px}
.socials span{width:18px;height:18px;border:2px solid #fff;border-radius:50%}
.footer-h{font-size:20px;font-weight:600;color:#fff}
.contact-list{list-style:none;margin-top:16px}
.contact-list li{display:flex;align-items:center;gap:16px;font-size:14px;margin-bottom:22px}
.contact-list .dot{width:30px;height:30px;border-radius:50%;background:#fff;display:flex;align-items:center;justify-content:center}
.newsletter-input{width:240px;height:38px;border:1px solid #777;border-radius:3px;margin-top:16px;padding:9px 12px;font-size:13px;color:var(--muted)}
.subscribe{margin-top:14px;background:var(--brown);color:#fff;border-radius:2px}
.copyright{left:0;top:3600px;width:1200px;text-align:center;font-size:13px;color:var(--muted)}
</style>
</head>
<body>

<!-- Hero -->
<div class="media hero-media" role="img" aria-label="Lit cigar resting with rising smoke against a dark backdrop"></div>
<div class="abs brand">VantorGoods</div>
<nav class="abs nav">
  <a class="active" href="#">Home</a><a href="#">About Us</a><a href="#">Products</a><a href="#">Contact Us</a>
</nav>
<div class="abs nav-icons">
  <svg width="22" height="22" viewBox="0 0 24 24" fill="none" stroke="#fff" stroke-width="1.8"><path d="M3 4h3l2.4 11h10l2-8H7"/><circle cx="10" cy="19" r="1.5"/><circle cx="17" cy="19" r="1.5"/></svg>
  <svg width="22" height="22" viewBox="0 0 24 24" fill="none" stroke="#fff" stroke-width="1.8"><circle cx="12" cy="8" r="4"/><path d="M4 21c1-4.5 4.5-6.5 8-6.5s7 2 8 6.5"/></svg>
</div>
<div class="abs hero-kicker serif">Welcome To</div>
<h1 class="abs hero-title serif">VantorGoods</h1>
<p class="abs hero-copy">A speakeasy, also called a blind pig or blind tiger, is an illicit establishment that sells alcoholic beverages, or a retro style bar that replicates aspects of historical speakeasies.</p>
<a class="abs btn hero-btn">Make a Reservation</a>

<!-- Portals -->
<div class="abs portal portal-consumer">
  <h2>Shop As A Consumer</h2>
  <p>Browse and Purchase Directly As An Individual</p>
  <a class="btn">Shop as a Consumer</a>
</div>
<div class="abs portal portal-business">
  <h2>Business Portal</h2>
  <p>Log In Or Apply For A B2B Account To Access Bulk Pricing</p>
  <a class="btn">Business Portal</a>
</div>

<!-- Story -->
<div class="abs story-head"><span></span><h2>Our Story</h2><span></span></div>
<p class="abs story-copy">The name "VantorGoods" will forever be associated with an experiment that failed the National Prohibition Act of 1920, better known as the 18th amendment. It was designed to improve health and cut crime but failed miserably. A small-town native authored much of the legislation to enforce Prohibition, known as the VantorGoods Act.</p>
<div class="media" style="left:120px;top:1064px;width:320px;height:408px;background:radial-gradient(circle at 55% 60%,#8a5a2a,#3a2414 55%,#151010)" role="img" aria-label="Cocktail and bottle with a cigar being lit"></div>
<div class="media" style="left:496px;top:1064px;width:224px;height:408px;background:linear-gradient(135deg,#1a2220,#243230 50%,#1a2220)" role="img" aria-label="Dark geometric lattice pattern"></div>
<div class="media" style="left:776px;top:1064px;width:320px;height:408px;background:radial-gradient(circle at 45% 65%,#9a6a25,#4a3012 50%,#141110)" role="img" aria-label="Glass of whiskey with a cigar and lighter"></div>

<!-- Oils -->
<div class="media" style="left:0;top:1600px;width:600px;height:480px;background:radial-gradient(ellipse at 50% 45%,#b89030,#5a4a20 45%,#2a2a1a 75%,var(--bg))" role="img" aria-label="Bottle of olive oil with spices and herbs"></div>
<div class="abs feature-title" style="left:652px;top:1724px;color:#fff"><span>Oils</span><i style="width:470px"></i></div>
<p class="abs feature-copy" style="left:652px;top:1800px;width:430px">Cold pressed in small batches, our oils are drawn from heritage groves and aged with patience. Each bottle carries a deep aroma and a smooth golden finish, chosen for the table, the bath and the careful host. We source from growers who tend their trees by hand and bottle only what meets our house standard of quality and character, season after season.</p>
<div class="abs rating" style="left:652px;top:1958px"><span class="stars">★★★★★</span>5 Star Rating</div>
<div class="abs shop-link" style="left:652px;top:1992px">Shop Now <svg width="30" height="10" viewBox="0 0 30 10" fill="none" stroke="#fff" stroke-width="1.5"><path d="M0 5h28M23 1l5 4-5 4"/></svg></div>

<!-- Cigar -->
<div class="abs feature-title" style="left:0;top:2290px;color:var(--gold-soft)"><i style="width:52px"></i><span>Cigar</span></div>
<p class="abs feature-copy" style="left:68px;top:2348px;width:500px">Hand rolled from long filler leaf and rested in cedar rooms, our cigars burn slow and even. Notes of cocoa, leather and toasted spice open with every draw. Each box is selected by our tobacconist from small family farms, then kept at steady humidity until the day it reaches your humidor, ready for a quiet evening and good company.</p>
<div class="abs rating" style="left:68px;top:2506px"><span class="stars">★★★★★</span>5 Star Rating</div>
<div class="abs shop-link" style="left:68px;top:2542px">Shop Now <svg width="30" height="10" viewBox="0 0 30 10" fill="none" stroke="#fff" stroke-width="1.5"><path d="M0 5h28M23 1l5 4-5 4"/></svg></div>
<div class="media" style="left:600px;top:2224px;width:600px;height:440px;background:radial-gradient(ellipse at 40% 45%,#a0703a,#5a3a1c 45%,#2a1c12 75%,var(--bg))" role="img" aria-label="Close-up of a cigar resting on a glass of whiskey"></div>

<!-- Products -->
<div class="abs product" style="left:68px">
  <div class="media" style="inset:0;background:radial-gradient(circle at 50% 35%,#7a4a28,#2e1d12 60%,#121010)" role="img" aria-label="Smoking cigar in an ashtray"></div>
  <div class="shade"></div>
  <div class="info"><h3>Cigar Accessories</h3><span class="stars">★★★★★</span><small>5 Star Rating</small><a class="btn">Shop Now</a></div>
</div>
<div class="abs product" style="left:434px">
  <div class="media" style="inset:0;background:radial-gradient(circle at 50% 35%,#5a4a4a,#2a2222 60%,#111)" role="img" aria-label="Perfume bottle with smoke"></div>
  <div class="shade"></div>
  <div class="info"><h3>Fragrances</h3><span class="stars">★★★★★</span><small>5 Star Rating</small><a class="btn">Shop Now</a></div>
</div>
<div class="abs product" style="left:800px">
  <div class="media" style="inset:0;background:radial-gradient(circle at 50% 35%,#8a7a2a,#3a3418 60%,#121210)" role="img" aria-label="Olive oil bottle with leaves"></div>
  <div class="shade"></div>
  <div class="info"><h3>Oils</h3><span class="stars">★★★★★</span><small>5 Star Rating</small><a class="btn">Shop Now</a></div>
</div>
<a class="abs btn view-all">View All Products</a>

<!-- Footer -->
<div class="abs footer-rule"></div>
<div class="abs footer-brand">VantorGoods</div>
<div class="abs socials"><span></span><span></span><span></span></div>
<div class="abs" style="left:460px;top:3376px">
  <div class="footer-h">Contact Us</div>
  <ul class="contact-list">
    <li><span class="dot"><svg width="14" height="14" viewBox="0 0 24 24" fill="#111"><path d="M6.6 10.8a15 15 0 0 0 6.6 6.6l2.2-2.2a1 1 0 0 1 1-.25 11 11 0 0 0 3.6.6 1 1 0 0 1 1 1V20a1 1 0 0 1-1 1A17 17 0 0 1 3 4a1 1 0 0 1 1-1h3.5a1 1 0 0 1 1 1 11 11 0 0 0 .6 3.6 1 1 0 0 1-.25 1z"/></svg></span>+1 (555) 010 4821</li>
    <li><span class="dot"><svg width="14" height="14" viewBox="0 0 24 24" fill="none" stroke="#111" stroke-width="2"><rect x="3" y="5" width="18" height="14" rx="1"/><path d="M3 6l9 7 9-7"/></svg></span>hello@vantorgoods.example</li>
    <li><span class="dot"><svg width="14" height="14" viewBox="0 0 24 24" fill="#111"><path d="M12 2a7 7 0 0 0-7 7c0 5 7 13 7 13s7-8 7-13a7 7 0 0 0-7-7zm0 9.5a2.5 2.5 0 1 1 0-5 2.5 2.5 0 0 1 0 5z"/></svg></span>123, Lorem Ipsum dolor</li>
  </ul>
</div>
<div class="abs" style="left:800px;top:3376px">
  <div class="footer-h">Subscribe To Our Newsletter</div>
  <div class="newsletter-input">E-Mail</div>
  <a class="btn subscribe">Subscribe</a>
</div>
<div class="abs copyright">Copyright©2024 VantorGoods. All rights reserved.</div>

</body>
</html>
```